Kanomiva business cards/stationary
Relocation Support Services
I need single sided standard sized Business Card [3.5" x 2"]
Designer's discretion
Professional
Ned Palmer
President
5-31-08 Nishimorino
Suginami-ku, Tokyo 168-0072
ned@kanomiva.com
www.kanomiva.com
Have not yet received logo files from designer. I will be using
Will upload Al format as soon as I receive from designer.
Kanomiva logo to be used

```html
<!DOCTYPE html>
<html lang="en">
<head>
<meta charset="utf-8">
<title>Kanomiva Stationery</title>
<link href="https://fonts.googleapis.com/css2?family=Open+Sans:wght@400;600;700;800&display=swap" rel="stylesheet">
<style>
  :root {
    --stage: #ebe8e3;
    --paper: #ffffff;
    --red: #b3191f;
    --red-dark: #6e0d12;
    --black: #1c1c1c;
    --grey: #9a9a9a;
    --grey-light: #e4e4e4;
    --text: #333333;
  }
  * { margin: 0; padding: 0; box-sizing: border-box; }
  html, body { width: 1200px; height: 871px; overflow: hidden; }
  body { background: var(--stage); font-family: "Open Sans", Arial, sans-serif; color: var(--text); position: relative; }

  .sheet { position: absolute; background: var(--paper); overflow: hidden; box-shadow: 0 2px 8px rgba(0,0,0,.18); }
  .sheet svg.swooshes { position: absolute; inset: 0; width: 100%; height: 100%; }

  .brand { position: absolute; display: flex; align-items: center; gap: 5px; }
  .brand-dot { border-radius: 50%; background: var(--red); }
  .brand-name { font-weight: 700; color: var(--red); letter-spacing: -.2px; }
  .brand-tagline { position: absolute; font-size: 6px; color: var(--grey); white-space: nowrap; }

  /* Letterhead */
  .letterhead { left: 36px; top: 67px; width: 540px; height: 732px; }
  .letterhead .brand { left: 22px; top: 34px; }
  .letterhead .brand-dot { width: 16px; height: 16px; }
  .letterhead .brand-name { font-size: 19px; }
  .letterhead .brand-tagline { left: 22px; top: 60px; }
  .letterhead .contact { position: absolute; left: 190px; top: 10px; font-size: 10px; line-height: 14px; font-weight: 600; color: var(--text); }
  .contact .label { color: var(--red); font-weight: 700; margin-right: 8px; }

  /* Business card */
  .card { left: 804px; top: 101px; width: 252px; height: 146px; border-radius: 10px; }
  .card .brand { left: 10px; top: 62px; }
  .card .brand-dot { width: 9px; height: 9px; }
  .card .brand-name { font-size: 13px; }
  .card .person { position: absolute; left: 108px; top: 8px; }
  .card .person-name { font-size: 27px; line-height: 27px; font-weight: 700; color: var(--red-dark); }
  .card .person-title { font-size: 12px; font-weight: 700; color: var(--black); margin-top: 2px; }
  .card .contact { position: absolute; left: 108px; top: 86px; font-size: 5.5px; line-height: 8px; color: var(--text); }

  /* Envelope */
  .envelope { left: 605px; top: 456px; width: 566px; height: 317px; }
  .envelope .brand { left: 247px; top: 24px; }
  .envelope .brand-dot { width: 10px; height: 10px; }
  .envelope .brand-name { font-size: 12px; }
  .envelope .brand-return { position: absolute; left: 20px; top: 194px; }
  .envelope .brand-return .brand-name { font-size: 15px; }
  .envelope .address { position: absolute; left: 20px; top: 220px; font-size: 10px; line-height: 14px; font-weight: 600; color: var(--text); }
</style>
</head>
<body>

<section class="sheet letterhead">
  <svg class="swooshes" viewBox="0 0 540 732" preserveAspectRatio="none">
    <defs>
      <linearGradient id="lh-red" x1="0" y1="0" x2="1" y2="0">
        <stop offset="0" stop-color="#e02a2f"/>
        <stop offset="1" stop-color="#6e0d12"/>
      </linearGradient>
    </defs>
    <path d="M540 0 H470 C405 150 395 500 500 732 H540 Z" fill="url(#lh-red)"/>
    <path d="M452 0 C384 150 374 500 482 732" fill="none" stroke="#1c1c1c" stroke-width="7"/>
    <path d="M436 0 C364 160 358 520 466 732" fill="none" stroke="#b5b5b5" stroke-width="3"/>
    <path d="M0 732 V585 C18 650 60 705 140 732 Z" fill="url(#lh-red)"/>
    <path d="M0 560 C20 640 75 708 170 732" fill="none" stroke="#1c1c1c" stroke-width="5"/>
    <path d="M0 540 C24 630 90 706 196 732" fill="none" stroke="#b5b5b5" stroke-width="2"/>
  </svg>
  <div class="brand"><span class="brand-dot"></span><span class="brand-name">Kanomiva</span></div>
  <div class="brand-tagline">Relocation Support Services</div>
  <div class="contact">
    <div><span class="label">Phone</span>+81 (0)80-5142-2086</div>
    <div><span class="label">Email</span>ned@kanomiva.com</div>
    <div><span class="label">Web address</span>www.kanomiva.com</div>
    <div>5-31-08 Nishimorino</div>
    <div>Suginami-ku, Tokyo 168-0072</div>
  </div>
</section>

<section class="sheet card">
  <svg class="swooshes" viewBox="0 0 252 146" preserveAspectRatio="none">
    <path d="M252 0 H118 C95 50 92 100 110 146 H252 Z" fill="var(--grey-light)"/>
    <path d="M100 146 C80 100 82 45 104 0" fill="none" stroke="#1c1c1c" stroke-width="2.5"/>
    <path d="M0 146 V112 C14 130 40 142 70 146 Z" fill="var(--red)"/>
  </svg>
  <div class="brand"><span class="brand-dot"></span><span class="brand-name">Kanomiva</span></div>
  <div class="person">
    <div class="person-name">Ned<br>Palmer</div>
    <div class="person-title">President</div>
  </div>
  <div class="contact">
    <div>Tel +81 (0)80-5142-2086</div>
    <div>ned@kanomiva.com</div>
    <div>www.kanomiva.com</div>
    <div>5-31-08 Nishimorino</div>
    <div>Suginami-ku, Tokyo 168-0072</div>
  </div>
</section>

<section class="sheet envelope">
  <svg class="swooshes" viewBox="0 0 566 317" preserveAspectRatio="none">
    <defs>
      <linearGradient id="env-red" x1="0" y1="0" x2="1" y2="0">
        <stop offset="0" stop-color="#e02a2f"/>
        <stop offset="1" stop-color="#6e0d12"/>
      </linearGradient>
    </defs>
    <rect x="0" y="0" width="566" height="6" fill="#f1f1f1"/>
    <path d="M566 60 C520 110 505 230 540 317 H566 Z" fill="url(#env-red)"/>
    <path d="M566 40 C505 100 488 230 522 317" fill="none" stroke="#1c1c1c" stroke-width="5"/>
    <path d="M566 25 C492 95 474 230 508 317" fill="none" stroke="#b5b5b5" stroke-width="2"/>
    <path d="M0 317 V255 C14 285 45 308 95 317 Z" fill="url(#env-red)"/>
    <path d="M0 240 C18 282 60 310 120 317" fill="none" stroke="#1c1c1c" stroke-width="4"/>
  </svg>
  <div class="brand"><span class="brand-dot"></span><span class="brand-name">Kanomiva</span></div>
  <div class="brand brand-return"><span class="brand-name">Kanomiva</span></div>
  <div class="address">
    <div>5-31-08 Nishimorino</div>
    <div>Suginami-ku, Tokyo 168-0072</div>
  </div>
</section>

</body>
</html>
```